San Francisco Pet Care Non Profit

Business Card Design for non profit organization.
We are a mobile pet care team who supports and attends to pets whose owners are homeless. Thanks for your help and creativity.

Industry/Entity Type

Non Profit

Contact Information for Business Card

Marisol Keddy
President
2871 Larkmoor Street, #512
San Francisco, CA 94187
phone: 415-729-3846
fax: 415-781-4052
marisol@tidywagonvan.org
website: tidywagonvan.org
facebook: facebook.com/TidyWagonVan

Font styles to use
Serif
Sans Serif

Colors

Designer to choose colors to be used in the design.

Requirements
Must have
• above details and attached logo

```html
<!DOCTYPE html>
<html lang="en">
<head>
<meta charset="utf-8">
<title>TidyWagonVan business cards</title>
<link href="https://fonts.googleapis.com/css2?family=Montserrat:wght@700&family=Open+Sans:wght@400;600;700&display=swap" rel="stylesheet">
<style>
  :root {
    --stage: #dcdde0;
    --brand-blue: #2aa8e0;
    --ink: #231f20;
    --paper: #ffffff;
  }
  * { margin: 0; padding: 0; box-sizing: border-box; }
  html, body { width: 1078px; height: 1200px; overflow: hidden; background: var(--stage); }
  body { position: relative; font-family: "Open Sans", sans-serif; color: var(--ink); }

  .card { position: absolute; border-radius: 18px; overflow: hidden; box-shadow: 0 2px 8px rgba(0,0,0,.08); }
  .card--blue { background: var(--brand-blue); }
  .card--white { background: var(--paper); }
  .card--tall { width: 253px; height: 444px; }
  .card--wide { width: 444px; height: 252px; }

  .card-front-tall { left: 266px; top: 75px; }
  .card-back-tall { left: 559px; top: 75px; }
  .card-front-large { left: 75px; top: 599px; }
  .card-front-small { left: 75px; top: 872px; }
  .card-back-wide { left: 559px; top: 736px; }

  .abs { position: absolute; }
  .center { left: 0; right: 0; text-align: center; }

  .mark-dot { position: absolute; border-radius: 50%; }
  .mark-dot--white { background: var(--paper); }
  .mark-dot--blue { background: var(--brand-blue); }
  .mark-dot--inline { position: static; flex: none; }

  .wordmark { font-family: "Montserrat", sans-serif; font-weight: 700; line-height: 1; white-space: nowrap; }
  .wordmark--white { color: var(--paper); }
  .wordmark--blue { color: var(--brand-blue); }
  .tagline { font-size: 12px; line-height: 1; white-space: nowrap; color: var(--ink); }
  .site-url { font-weight: 700; color: var(--paper); font-size: 12px; letter-spacing: .6px; white-space: nowrap; }

  .brand-stack { display: flex; flex-direction: column; align-items: center; }
  .brand-lockup { display: flex; align-items: center; gap: 10px; }

  .person-name { color: var(--brand-blue); font-weight: 700; font-size: 15px; letter-spacing: .3px; }
  .person-title { font-size: 10.5px; }
  .contact { font-size: 10.5px; line-height: 16.5px; }
  .rule-blue { height: 1.5px; background: var(--brand-blue); }
  .rule-ink { height: 1.5px; background: var(--ink); }

  .icon-row { display: flex; gap: 5px; justify-content: center; }
  .icon-ring { width: 20px; height: 20px; border: 1.4px solid var(--brand-blue); border-radius: 50%; display: flex; align-items: center; justify-content: center; }
  .icon-ring svg { width: 11px; height: 11px; fill: var(--brand-blue); }

  .contact-line { display: flex; align-items: center; gap: 5px; font-size: 10.5px; line-height: 16px; }
  .contact-line svg { width: 10px; height: 10px; fill: var(--brand-blue); }

  .bar { position: absolute; bottom: 0; height: 8px; }
</style>
</head>
<body>

<!-- Tall front -->
<section class="card card--blue card--tall card-front-tall">
  <div class="mark-dot mark-dot--white" style="left:87px;top:138px;width:80px;height:80px;"></div>
  <div class="abs center wordmark wordmark--white" style="top:270px;font-size:24px;">TidyWagonVan</div>
  <div class="abs center tagline" style="top:297px;">Mobile Pet Care Team</div>
  <div class="abs center site-url" style="top:406px;">TIDYWAGONVAN.ORG</div>
</section>

<!-- Tall back -->
<section class="card card--white card--tall card-back-tall">
  <div class="mark-dot mark-dot--blue" style="left:86px;top:75px;width:80px;height:80px;"></div>
  <div class="abs center person-name" style="top:194px;">MARISOL KEDDY</div>
  <div class="abs center person-title" style="top:212px;">PRESIDENT</div>
  <div class="abs rule-blue" style="left:90px;width:72px;top:239px;"></div>
  <div class="abs center contact" style="top:251px;">2871 Larkmoor Street, #512<br>San Francisco, CA 94187</div>
  <div class="abs center icon-row" style="top:292px;">
    <span class="icon-ring"><svg viewBox="0 0 24 24"><path d="M6.6 10.8a15 15 0 0 0 6.6 6.6l2.2-2.2c.3-.3.7-.4 1-.2 1.1.4 2.3.6 3.6.6.6 0 1 .4 1 1V20c0 .6-.4 1-1 1A17 17 0 0 1 3 4c0-.6.4-1 1-1h3.5c.6 0 1 .4 1 1 0 1.3.2 2.5.6 3.6.1.3 0 .7-.2 1z"/></svg></span>
    <span class="icon-ring"><svg viewBox="0 0 24 24"><path d="M6 2h12v5H6zM4 8h16a2 2 0 0 1 2 2v7h-4v5H6v-5H2v-7a2 2 0 0 1 2-2zm4 8v4h8v-4z"/></svg></span>
    <span class="icon-ring"><svg viewBox="0 0 24 24"><path d="M2 5h20v14H2zm2 2v.5l8 5 8-5V7z"/></svg></span>
    <span class="icon-ring"></span>
  </div>
  <div class="abs center contact" style="top:322px;">415-729-3846<br>415-781-4052<br>marisol@tidywagonvan.org<br>facebook.com/TidyWagonVan</div>
  <div class="bar" style="left:0;right:0;background:var(--brand-blue);"></div>
</section>

<!-- Large front -->
<section class="card card--blue card--wide card-front-large">
  <div class="mark-dot mark-dot--white" style="left:40px;top:45px;width:150px;height:150px;"></div>
  <div class="abs brand-stack" style="left:196px;width:230px;top:164px;">
    <div class="wordmark wordmark--white" style="font-size:27px;">TidyWagonVan</div>
    <div class="tagline" style="font-size:13.5px;margin-top:4px;">Mobile Pet Care Team</div>
    <div class="site-url" style="font-size:13px;letter-spacing:.2px;margin-top:6px;">TidyWagonVan.org</div>
  </div>
</section>

<!-- Small front -->
<section class="card card--blue card--wide card-front-small">
  <div class="abs" style="left:0;right:0;top:98px;display:flex;justify-content:center;">
    <div class="brand-lockup" style="gap:14px;">
      <div class="mark-dot mark-dot--white mark-dot--inline" style="width:54px;height:54px;"></div>
      <div class="brand-stack">
        <div class="wordmark wordmark--white" style="font-size:30px;">TidyWagonVan</div>
        <div class="tagline" style="font-size:15px;margin-top:4px;">Mobile Pet Care Team</div>
      </div>
    </div>
  </div>
  <div class="abs center site-url" style="top:218px;font-size:13px;letter-spacing:.2px;">www.TIDYWAGONVAN.org</div>
</section>

<!-- Wide back -->
<section class="card card--white card--wide card-back-wide">
  <div class="abs brand-lockup" style="right:26px;top:18px;">
    <div class="mark-dot mark-dot--blue mark-dot--inline" style="width:46px;height:46px;"></div>
    <div class="brand-stack">
      <div class="wordmark wordmark--blue" style="font-size:25px;">TidyWagonVan</div>
      <div class="tagline" style="font-weight:700;font-size:13px;margin-top:3px;">Mobile Pet Care Team</div>
    </div>
  </div>
  <div class="abs person-name" style="left:26px;top:128px;">MARISOL KEDDY</div>
  <div class="abs person-title" style="left:26px;top:146px;">PRESIDENT</div>
  <div class="abs rule-ink" style="left:26px;right:26px;top:169px;"></div>
  <div class="abs" style="left:26px;top:179px;">
    <div class="contact-line"><svg viewBox="0 0 24 24"><path d="M6.6 10.8a15 15 0 0 0 6.6 6.6l2.2-2.2c.3-.3.7-.4 1-.2 1.1.4 2.3.6 3.6.6.6 0 1 .4 1 1V20c0 .6-.4 1-1 1A17 17 0 0 1 3 4c0-.6.4-1 1-1h3.5c.6 0 1 .4 1 1 0 1.3.2 2.5.6 3.6.1.3 0 .7-.2 1z"/></svg>415-729-3846</div>
    <div class="contact-line"><svg viewBox="0 0 24 24"><path d="M6 2h12v5H6zM4 8h16a2 2 0 0 1 2 2v7h-4v5H6v-5H2v-7a2 2 0 0 1 2-2zm4 8v4h8v-4z"/></svg>415-781-4052</div>
    <div class="contact-line"><svg viewBox="0 0 24 24"><path d="M2 5h20v14H2zm2 2v.5l8 5 8-5V7z"/></svg>marisol@tidywagonvan.org</div>
  </div>
  <div class="abs contact" style="right:26px;top:179px;text-align:right;line-height:16px;">2871 Larkmoor Street, #512<br>San Francisco, CA 94187<br>facebook.com/TidyWagonVan</div>
  <div class="bar" style="left:0;width:222px;background:var(--brand-blue);"></div>
  <div class="bar" style="left:222px;right:0;background:var(--ink);"></div>
</section>

</body>
</html>
```